Computer background screen

I've attached our current background I'm looking for a new designs We can use. check out our website and social media for ideas. www.brightcoreservices.com

Requirements
Must have
• NEED WASHINGTON DC SKYLINE IN PICTURE W/ LOGO

```html
<!DOCTYPE html>
<html lang="en">
<head>
<meta charset="utf-8">
<title>BrightCore Services – Background Screen &amp; Social Media Banner</title>
<link href="https://fonts.googleapis.com/css2?family=Montserrat:wght@400;600;700&display=swap" rel="stylesheet">
<style>
  :root {
    --canvas: #d4d4d4;
    --canvas-light: #e8e6e6;
    --navy: #0a2a8c;
    --red: #e3141b;
    --ink: #1f1f1f;
    --grey-text: #3a3a3a;
    --panel: #f3f3f5;
    --strip: #e9e9ec;
    --photo-dark: #1e242b;
    --photo-mid: #4a5560;
    --photo-light: #8a949c;
  }
  * { box-sizing: border-box; margin: 0; padding: 0; }
  html, body { width: 730px; height: 1200px; overflow: hidden; }
  body {
    font-family: "Montserrat", sans-serif;
    background: linear-gradient(160deg, var(--canvas) 0%, var(--canvas) 45%, var(--canvas-light) 45%, var(--canvas-light) 100%);
    position: relative;
  }
  .section-title {
    position: absolute; left: 0; width: 730px; text-align: center;
    font-weight: 700; font-size: 18px; color: var(--ink); letter-spacing: 0.3px;
  }

  /* Background screen */
  .background-screen {
    position: absolute; left: 45px; top: 90px; width: 640px; height: 400px;
    overflow: hidden; box-shadow: 0 6px 18px rgba(0,0,0,0.25);
  }
  .city-photo {
    position: absolute; inset: 0;
    background:
      radial-gradient(ellipse at 55% 95%, rgba(230,80,90,0.35), transparent 45%),
      radial-gradient(ellipse at 50% 75%, rgba(240,235,220,0.35), transparent 40%),
      linear-gradient(180deg, var(--photo-light) 0%, var(--photo-mid) 40%, var(--photo-dark) 100%);
  }
  .screen-brand {
    position: absolute; left: 0; right: 0; top: 292px; text-align: center;
    font-weight: 700; font-size: 30px; color: var(--red); letter-spacing: 0.5px;
  }

  /* Social media banner */
  .social-banner {
    position: absolute; left: 25px; top: 590px; width: 680px; height: 252px;
    overflow: hidden; background: var(--panel);
    box-shadow: 0 6px 18px rgba(0,0,0,0.2);
  }
  .social-banner .city-photo { left: 150px; }
  .banner-swoosh { position: absolute; inset: 0; }
  .banner-kicker {
    position: absolute; left: 27px; top: 42px; font-size: 13px; color: var(--grey-text);
  }
  .banner-headline {
    position: absolute; left: 27px; top: 56px; font-size: 22px; font-weight: 700; color: var(--ink);
  }
  .service {
    position: absolute; text-align: center; font-size: 10px; color: var(--grey-text);
  }
  .service svg { display: block; margin: 0 auto 6px; }
  .service-divider { position: absolute; width: 1px; background: #cfcfd4; }
  .service-rule { position: absolute; height: 1px; background: #cfcfd4; left: 18px; width: 232px; top: 154px; }
  .contact-strip {
    position: absolute; left: 290px; right: 0; bottom: 0; height: 32px; background: var(--strip);
    display: flex; align-items: center; justify-content: space-evenly;
    font-size: 10px; font-weight: 700; color: var(--ink);
  }
  .contact-item { display: flex; align-items: center; gap: 5px; }
  .contact-dot {
    width: 18px; height: 18px; border-radius: 50%; background: var(--red);
    display: flex; align-items: center; justify-content: center;
  }
</style>
</head>
<body>

  <section class="background-screen">
    <div class="city-photo" role="img" aria-label="Night photograph of a city highway with streetlights, tall buildings and red and white light trails"></div>
    <div class="screen-brand">BrightCore Services</div>
  </section>
  <h2 class="section-title" style="top:515px">Background Screen</h2>

  <section class="social-banner">
    <div class="city-photo" role="img" aria-label="Night photograph of a city highway lined with streetlights and light trails"></div>
    <svg class="banner-swoosh" width="680" height="252" viewBox="0 0 680 252">
      <path d="M0 0 H140 C180 40 250 50 275 110 C300 170 290 220 305 252 H0 Z" fill="var(--panel)"/>
      <path d="M135 0 H170 C230 30 260 50 280 110 C295 160 285 215 305 252 H298 C280 215 292 165 274 115 C255 60 200 40 135 0 Z" fill="var(--red)"/>
      <path d="M135 0 H160 C215 25 245 45 262 80 C235 50 190 30 135 0 Z" fill="var(--navy)"/>
      <path d="M0 215 C8 225 12 240 14 252 H0 Z" fill="var(--navy)"/>
    </svg>

    <p class="banner-kicker">Trusted And Reliable</p>
    <h1 class="banner-headline">Lighting Expert</h1>

    <div class="service" style="left:18px; top:98px; width:72px">
      <svg width="26" height="32" viewBox="0 0 26 32"><path d="M3 4 H23 M13 4 V30 M8 30 H18" stroke="var(--navy)" stroke-width="3" fill="none"/></svg>
      Road Way
    </div>
    <div class="service-divider" style="left:78px; top:98px; height:52px"></div>
    <div class="service" style="left:86px; top:98px; width:92px">
      <svg width="26" height="32" viewBox="0 0 26 32"><rect x="4" y="2" width="14" height="8" fill="var(--navy)"/><path d="M11 10 V30 M6 30 H16" stroke="var(--navy)" stroke-width="3"/></svg>
      Sports Lighting
    </div>
    <div class="service-divider" style="left:170px; top:98px; height:52px"></div>
    <div class="service" style="left:176px; top:98px; width:86px">
      <svg width="32" height="32" viewBox="0 0 32 32"><circle cx="16" cy="14" r="7" fill="var(--navy)"/><rect x="13" y="22" width="6" height="6" fill="var(--navy)"/><path d="M16 1 V4 M4 14 H7 M25 14 H28 M7 5 L9 7 M25 5 L23 7" stroke="var(--navy)" stroke-width="2"/></svg>
      Led Upgrades
    </div>
    <div class="service-rule"></div>
    <div class="service" style="left:60px; top:166px; width:86px; font-size:11px">
      <svg width="30" height="30" viewBox="0 0 30 30"><path d="M3 12 L15 3 L27 12 V28 H3 Z" fill="none" stroke="var(--navy)" stroke-width="3"/><rect x="10" y="16" width="10" height="10" fill="var(--navy)"/></svg>
      Wareshoue
    </div>
    <div class="service-divider" style="left:156px; top:166px; height:52px"></div>
    <div class="service" style="left:160px; top:166px; width:86px; font-size:11px">
      <svg width="32" height="32" viewBox="0 0 32 32"><circle cx="16" cy="14" r="8" fill="var(--navy)"/><path d="M17 8 L13 15 H18 L15 21" stroke="#fff" stroke-width="2" fill="none"/><path d="M16 1 V4 M3 14 H6 M26 14 H29" stroke="var(--navy)" stroke-width="2"/></svg>
      Electrical
    </div>

    <div class="contact-strip">
      <span class="contact-item">CALL US
        <span class="contact-dot"><svg width="10" height="10" viewBox="0 0 10 10"><path d="M2 1 L4 1 L5 3 L4 4 C5 6 6 6 6 6 L7 5 L9 6 V8 C5 9 1 5 2 1 Z" fill="#fff"/></svg></span>
        555. 014.2290</span>
      <span class="contact-item">
        <span class="contact-dot"><svg width="10" height="10" viewBox="0 0 10 10"><circle cx="5" cy="5" r="4" fill="none" stroke="#fff" stroke-width="1.2"/><path d="M1 5 H9 M5 1 V9" stroke="#fff" stroke-width="1"/></svg></span>
        BRIGHTCORESERVICES.COM</span>
    </div>
  </section>
  <h2 class="section-title" style="top:878px">Social Media Banner</h2>

</body>
</html>
```